Business Card Design Project

I own a dental practice and would like to use a logo that was recently designed to make business cards.
I am looking for a clean card with the following information on the card.

Halvorsen Dental Center (Using the logo)
Martin L. Halvorsen, D.D.S.
7234 Pinewick Ave. Suite B
Colorado Springs, CO 80547
(719) 482-6130
halvorsendentalcenter@mailbox-example.net
www.halvorsendentalcenter.example

Also a list of items on the back:
Services include

Family Dentistry
Cosmetic
Whitening
Tooth Colored Fillings
Crowns/Bridges
Implants/Tooth Replacement
Dentures
Root Canals
Updates

Just an FYI, I added an email address and website address.

I also added my Pic.  Please give designs with and without the pic

Thanks

Target Market(s)

20-70 U.S. Female that handles the household budget.

Industry/Entity Type

Dental

Requirements
Must have
• The logo is key. The color scheme of the logo is also key. The back of the business card should have the list of Dental Services offered at the practice. The front should be clean and professional looking. No cartoons. I will also include a picture of myself. I think that the final card may or may not include this picture, so the card designs should come with and without the picture. USE THE BLUE LOGO ONLY!!!
Should not have
• NO teeth should be on the card.

```html
<!DOCTYPE html>
<html lang="en">
<head>
<meta charset="utf-8">
<title>Halvorsen Dental Center – Business Card Options</title>
<link rel="stylesheet" href="https://fonts.googleapis.com/css2?family=Source+Sans+3:ital,wght@0,400;0,600;0,700;1,400&family=Crimson+Pro:wght@400&display=swap">
<style>
  :root {
    --stage: #5e4030;
    --paper: #ffffff;
    --ink: #3a3a3a;
    --brand-blue: #6f95a5;
    --brand-brown: #5d4b43;
    --teal-deep: #2c5260;
    --teal-mid: #557a89;
    --teal-light: #8fa9b5;
    --label: #ffffff;
  }
  * { box-sizing: border-box; margin: 0; padding: 0; }
  html, body { width: 1200px; height: 781px; overflow: hidden; }
  body {
    position: relative;
    background: var(--stage);
    font-family: "Source Sans 3", "Helvetica Neue", Arial, sans-serif;
    color: var(--ink);
  }
  .option-label {
    position: absolute;
    width: 300px;
    text-align: center;
    font-size: 26px;
    color: var(--label);
    font-weight: 400;
  }
  .card {
    position: absolute;
    width: 516px;
    height: 294px;
    overflow: hidden;
    background: var(--paper);
    box-shadow: 0 3px 8px rgba(0,0,0,.35);
  }
  /* Front */
  .brand {
    position: absolute;
    left: 26px; top: 24px;
    display: flex; align-items: center; gap: 12px;
  }
  .brand-dot {
    width: 40px; height: 40px; border-radius: 50%;
    background: var(--brand-blue);
  }
  .brand-name {
    font-size: 27px; line-height: 1.05;
    font-weight: 400; color: var(--brand-blue);
  }
  .address {
    position: absolute; left: 26px; top: 144px;
    font-size: 14px;
  }
  .contact-list {
    position: absolute; left: 26px; top: 178px;
    list-style: none; font-size: 13.5px;
  }
  .contact-list li { display: flex; align-items: center; gap: 7px; height: 22.5px; }
  .contact-list svg { width: 11px; height: 11px; flex: none; }
  .swoosh { position: absolute; left: 0; top: 0; width: 516px; height: 294px; }
  .doctor {
    position: absolute; right: 26px; top: 252px;
    text-align: right; color: var(--paper);
  }
  .doctor-name { font-size: 19px; font-weight: 700; line-height: 1; }
  .doctor-title { font-size: 13px; line-height: 1.3; margin-top: 2px; }
  .portrait {
    position: absolute; left: 340px; top: 40px;
    width: 180px; height: 190px;
    background: linear-gradient(180deg, #b98a72 0 55%, #2b2a33 68%);
    clip-path: path("M95 12 C125 12 140 40 138 72 C136 100 122 120 108 128 L150 140 C168 146 180 160 180 190 L20 190 C22 160 40 146 62 140 L82 128 C66 118 52 98 52 72 C50 40 65 12 95 12Z");
  }
  /* Back */
  .services-heading { font-size: 19px; font-weight: 600; color: var(--paper); }
  .services-list { list-style: none; color: #eef3f5; font-size: 15px; }
  .services-list li { height: 24.8px; display: flex; align-items: center; }
  .services-list li::before {
    content: ""; width: 7px; height: 7px; border-radius: 50%;
    background: currentColor; margin-right: 6px;
  }
  .back-split { display: flex; }
  .services-panel {
    position: relative; width: 258px; height: 100%;
    background: linear-gradient(90deg, var(--teal-deep), var(--teal-mid) 70%, var(--teal-light));
    padding: 34px 0 0 42px;
  }
  .services-panel .services-heading { margin-bottom: 9px; }
  .appointment { position: relative; flex: 1; padding: 24px 0 0 13px; font-size: 14px; }
  .appointment-title {
    font-family: "Crimson Pro", Georgia, serif;
    font-size: 19px; letter-spacing: 1px; margin-bottom: 14px;
  }
  .field { display: flex; align-items: flex-end; height: 33px; }
  .rule { border-bottom: 1px solid #777; height: 1px; margin: 0 4px 3px; }
  .box { display: inline-block; border: 1px solid #555; height: 18px; }
  .days { display: grid; grid-template-columns: repeat(3, auto); justify-content: start; column-gap: 10px; row-gap: 10px; margin-top: 16px; font-size: 13px; }
  .day { display: flex; align-items: center; gap: 6px; }
  .day .box { width: 30px; }
  .note { margin-top: 18px; font-style: italic; font-size: 14px; line-height: 1.3; color: #555; }
  .back-full {
    background: radial-gradient(circle at 26% 50%, var(--teal-light) 0, var(--teal-mid) 35%, var(--teal-deep) 85%);
  }
  .back-full .brand-mark {
    position: absolute; left: 70px; top: 75px;
    width: 140px; height: 140px; border-radius: 50%;
    background: rgba(255,255,255,.18);
  }
  .back-full .services { position: absolute; left: 281px; top: 40px; }
  .back-full .services-heading { margin-bottom: 6px; }
</style>
</head>
<body>

<div class="option-label" style="left:150px; top:16px;">Option # 2</div>
<div class="option-label" style="left:690px; top:16px;">Option # 1</div>
<div class="option-label" style="left:150px; top:742px;">Option # 2</div>
<div class="option-label" style="left:690px; top:742px;">Option # 1</div>

<svg width="0" height="0" style="position:absolute">
  <defs>
    <symbol id="icon-phone" viewBox="0 0 12 12"><circle cx="6" cy="6" r="5.3" fill="none" stroke="#444" stroke-width="1.1"/><path d="M4 3.3 5 3l.6 1.5-.7.5a4 4 0 0 0 2 2l.5-.7 1.5.6-.3 1A1 1 0 0 1 7.8 8.6 5 5 0 0 1 3.4 4.2 1 1 0 0 1 4 3.3Z" fill="#444"/></symbol>
    <symbol id="icon-mail" viewBox="0 0 12 12"><path d="M1 4.5 6 1.5l5 3V10H1Z" fill="#444"/><path d="M1.8 4.8 6 7.3l4.2-2.5" fill="none" stroke="#fff" stroke-width=".9"/></symbol>
    <symbol id="icon-web" viewBox="0 0 12 12"><circle cx="6" cy="6" r="5.3" fill="#444"/><path d="M.8 6h10.4M6 .8c-2.6 3-2.6 7.4 0 10.4M6 .8c2.6 3 2.6 7.4 0 10.4" fill="none" stroke="#fff" stroke-width=".8"/></symbol>
    <symbol id="card-swoosh" viewBox="0 0 516 294">
      <path d="M0 272C150 292 300 228 516 228L516 294 0 294Z" fill="var(--brand-brown)"/>
      <path d="M0 282C170 296 320 240 516 242L516 294 0 294Z" fill="#fff"/>
      <path d="M0 286C180 298 330 246 516 247L516 294 0 294Z" fill="var(--brand-blue)"/>
      <path d="M150 286C260 266 360 236 470 228" fill="none" stroke="#fff" stroke-width="1.2" opacity=".8"/>
    </symbol>
  </defs>
</svg>

<!-- Front without portrait -->
<section class="card card-front" style="left:57px; top:86px;">
  <div class="brand"><span class="brand-dot"></span><span class="brand-name">Halvorsen<br>Dental Center</span></div>
  <p class="address">7234 Pinewick Ave. Suite B, Colorado Springs, CO 80547</p>
  <ul class="contact-list">
    <li><svg><use href="#icon-phone"/></svg>(719) 482-6130</li>
    <li><svg><use href="#icon-mail"/></svg>halvorsendentalcenter@mailbox-example.net</li>
    <li><svg><use href="#icon-web"/></svg>www.halvorsendentalcenter.example</li>
  </ul>
  <svg class="swoosh"><use href="#card-swoosh"/></svg>
  <div class="doctor"><div class="doctor-name">Martin L. Halvorsen</div><div class="doctor-title">D.D.S.</div></div>
</section>

<!-- Front with portrait -->
<section class="card card-front" style="left:640px; top:86px;">
  <div class="brand"><span class="brand-dot"></span><span class="brand-name">Halvorsen<br>Dental Center</span></div>
  <div class="portrait" role="img" aria-label="Portrait photo of Dr. Martin L. Halvorsen in a dark suit"></div>
  <p class="address">7234 Pinewick Ave. Suite B, Colorado Springs, CO 80547</p>
  <ul class="contact-list">
    <li><svg><use href="#icon-phone"/></svg>(719) 482-6130</li>
    <li><svg><use href="#icon-mail"/></svg>halvorsendentalcenter@mailbox-example.net</li>
    <li><svg><use href="#icon-web"/></svg>www.halvorsendentalcenter.example</li>
  </ul>
  <svg class="swoosh"><use href="#card-swoosh"/></svg>
  <div class="doctor"><div class="doctor-name">Martin L. Halvorsen</div><div class="doctor-title">D.D.S.</div></div>
</section>

<!-- Back with appointment form -->
<section class="card back-split" style="left:59px; top:410px;">
  <div class="services-panel">
    <h2 class="services-heading">List of Services</h2>
    <ul class="services-list">
      <li>Family Dentistry</li><li>Cosmetic</li><li>Whitening</li><li>Tooth Colored Fillings</li>
      <li>Crowns/Bridges</li><li>Implants/Tooth Replacement</li><li>Dentures</li><li>Root Canals</li>
    </ul>
  </div>
  <div class="appointment">
    <h2 class="appointment-title">YOUR APPOINTMENT</h2>
    <div class="field">Name:<span class="rule" style="width:190px"></span></div>
    <div class="field">Date :<span class="rule" style="width:60px"></span>Time :<span class="rule" style="width:50px"></span><small>am/pm</small></div>
    <div class="field">Next Appointment&nbsp;<span class="box" style="width:94px; height:20px"></span></div>
    <div class="days">
      <span class="day">MON <span class="box"></span></span>
      <span class="day">TUE <span class="box"></span></span>
      <span class="day">WED <span class="box"></span></span>
      <span class="day">THU <span class="box"></span></span>
      <span class="day">FRI <span class="box"></span></span>
      <span class="day">SAT <span class="box"></span></span>
    </div>
    <p class="note">We appreciate a 24 hr.<br>notice for cancellations</p>
  </div>
</section>

<!-- Back full -->
<section class="card back-full" style="left:629px; top:418px;">
  <span class="brand-mark"></span>
  <div class="services">
    <h2 class="services-heading">list of Services</h2>
    <ul class="services-list">
      <li>Family Dentistry</li><li>Cosmetic</li><li>Whitening</li><li>Tooth Colored Fillings</li>
      <li>Crowns/Bridges</li><li>Implants/Tooth Replacement</li><li>Dentures</li><li>Root Canals</li>
    </ul>
  </div>
</section>

</body>
</html>
```